Hualuoya herb bottle label

we need a new label design to reflect our branding for our Chinese herbal medicine product bottles. We import herbs from China and distribute them to Australian Practitioners. The product may be visible to their clients so we want to present it well. Our branding colours and images are attached below, as is the current label layout template. The manufacturer adds the individual names of the herbs and other details over the top so the back ground must be subtle. We would like our name - HuaLuoya at the top to possibly be in yellow/gold and in our chosen font (it will need to be saved and inserted as an image as last print run it reverted to a default font). we would like the blue mountains of the picture below incorporated as the back ground colours. The design needs to feel traditional and artistic. Our name Hualuoya means - essence and spirit. We represent the essence and spirit of traditional Chinese herbal medicine.

```html
<!DOCTYPE html>
<html lang="en">
<head>
<meta charset="utf-8">
<title>Hualuoya herb bottle label</title>
<link href="https://fonts.googleapis.com/css2?family=Poiret+One&family=Montserrat:wght@300;400;700&display=swap" rel="stylesheet">
<style>
  :root{
    --page:#eef0f2;
    --sky-top:#4ec6f2;
    --sky-mid:#bfe6f7;
    --mist:#9cc8e8;
    --ridge:#3f86c9;
    --ridge-deep:#2a64ad;
    --gold:#f5d90a;
    --seal:#e23a2a;
    --seal-edge:#f2a091;
    --band:#e8202a;
    --white:#ffffff;
    --ink:#2a2a2a;
  }
  *{margin:0;padding:0;box-sizing:border-box;}
  html,body{width:1067px;height:1200px;overflow:hidden;background:var(--page);}
  .canvas{position:relative;width:1067px;height:1200px;}
  .label{
    position:absolute;left:0;top:399px;width:1067px;height:402px;overflow:hidden;
    font-family:"Montserrat",sans-serif;color:var(--white);
  }
  .scenery{
    position:absolute;inset:0;
    background:linear-gradient(180deg,var(--sky-top) 0%,var(--sky-mid) 52%,var(--mist) 68%,var(--ridge) 84%,var(--ridge-deep) 100%);
  }
  .band{position:absolute;left:0;width:1067px;background:var(--band);}
  .band--upper{top:130px;height:15px;}
  .band--lower{top:159px;height:11px;}
  .seal{
    position:absolute;background:var(--seal);border:2px solid var(--seal-edge);
    display:flex;align-items:center;justify-content:center;
    writing-mode:vertical-rl;font-family:"Poiret One",sans-serif;color:var(--white);
    letter-spacing:2px;box-shadow:0 0 0 4px var(--sky-mid);
  }
  .seal--side{width:46px;height:106px;top:92px;font-size:15px;}
  .seal--left{left:155px;}
  .seal--right{left:819px;}
  .seal--main{left:476px;top:92px;width:68px;height:152px;font-size:22px;}
  .brand{position:absolute;left:370px;top:26px;width:296px;text-align:center;color:var(--gold);font-family:"Poiret One",sans-serif;}
  .brand__name{font-size:40px;line-height:40px;letter-spacing:1px;font-weight:400;}
  .brand__tag{font-size:15px;line-height:18px;margin-top:1px;}
  .product-type{position:absolute;left:720px;top:36px;font-size:17px;line-height:19px;font-weight:300;}
  .dispensing{position:absolute;left:720px;top:232px;font-size:15px;font-weight:300;}
  .address{position:absolute;left:720px;top:262px;font-size:13.5px;line-height:17.4px;font-weight:300;font-style:normal;}
  .origin{position:absolute;left:720px;top:356px;font-size:16px;font-weight:700;}
  .net{position:absolute;left:440px;top:350px;width:156px;text-align:center;font-size:21px;font-weight:700;}
  .maker{position:absolute;left:612px;top:328px;width:80px;text-align:center;font-size:11px;font-weight:400;}
  .maker__dot{display:block;width:22px;height:22px;border-radius:50%;background:var(--seal);margin:0 auto 4px;}
  .record{position:absolute;left:19px;top:308px;width:180px;height:94px;background:var(--white);color:var(--ink);font-size:15px;font-weight:300;padding:16px 0 0 13px;line-height:31px;}
</style>
</head>
<body>
<div class="canvas">
  <section class="label">
    <div class="scenery" role="img" aria-label="Misty blue mountain ridges under a pale sky, with a bare tree branch at top left and a flock of birds in flight"></div>
    <div class="band band--upper"></div>
    <div class="band band--lower"></div>
    <div class="seal seal--side seal--left">Hualuoya</div>
    <div class="seal seal--main">Hualuoya</div>
    <div class="seal seal--side seal--right">Hualuoya</div>
    <header class="brand">
      <h1 class="brand__name">HUALUOYA</h1>
      <p class="brand__tag">Concentrated Chinese Herbs</p>
    </header>
    <p class="product-type">Single Herb Granules<br>Concentrated Extract 5:1</p>
    <p class="dispensing">Bulk for Practitioner Dispensing Only</p>
    <address class="address">
      Qinghe Pharmaceutical Co. LTD. China<br>
      Distributed by Hua Luoya Pty. Ltd.<br>
      118 Ridgeview Road<br>
      Darlington WA 6070<br>
      Australia
    </address>
    <p class="origin">Product of China</p>
    <p class="net">100g NET</p>
    <div class="maker"><span class="maker__dot"></span>Hualuoya</div>
    <div class="record">BATCH NO:<br>USE BY:</div>
  </section>
</div>
</body>
</html>
```